Special release wine label

Marrow Creek Vineyards is a small premium wine producer in the Barossa - South Australia. We are a five star rated winery, producing exceptional wines true to variety, region and house style. We have a very special parcel of wine that we wish to release as an exclusive wine. Visit www.marrowcreekvineyards.com.au for further feel.

The wine will be called Marrow Creek Vineyards, 2012, The Quiet Harvest Shiraz - Cabernet.

The wine can be bottled in either a burgundy or Bordeaux shaped bottle

Industry/Entity Type

House

```html
<!DOCTYPE html>
<html lang="en">
<head>
<meta charset="utf-8">
<title>Marrow Creek Vineyards – The Quiet Harvest Shiraz-Cabernet 2012</title>
<link rel="stylesheet" href="https://fonts.googleapis.com/css2?family=Marcellus+SC&family=Herr+Von+Muellerhoff&display=swap">
<style>
  :root {
    --backdrop: #f4f1ea;
    --label-wine: #5a0e2d;
    --label-ink: #ffffff;
    --estate-gold: #f2d65c;
    --estate-gold-deep: #d9b43c;
  }
  * { margin: 0; padding: 0; box-sizing: border-box; }
  html, body {
    width: 1200px;
    height: 1000px;
    overflow: hidden;
    background: var(--backdrop);
  }
  .canvas {
    position: relative;
    width: 1200px;
    height: 1000px;
  }
  .wine-label {
    position: absolute;
    left: 301px;
    top: 95px;
    width: 598px;
    height: 810px;
    background: var(--label-wine);
    border-radius: 26px;
    color: var(--label-ink);
    text-align: center;
  }
  .estate-illustration {
    position: absolute;
    left: 144px;
    top: 68px;
    width: 318px;
    height: 248px;
    border-radius: 6px;
    background: radial-gradient(ellipse at 50% 60%, var(--estate-gold) 0%, var(--estate-gold-deep) 55%, rgba(217,180,60,0.15) 100%);
    opacity: 0.85;
  }
  .winery-name {
    position: absolute;
    left: 0;
    right: 0;
    top: 350px;
    font-family: "Marcellus SC", "Times New Roman", serif;
    font-size: 27px;
    line-height: 37px;
    letter-spacing: 3px;
  }
  .winery-name span { display: block; }
  .vintage {
    position: absolute;
    left: 270px;
    top: 438px;
    width: 58px;
    height: 27px;
    border: 1.5px solid var(--label-ink);
    border-radius: 50%;
    font-family: "Marcellus SC", "Times New Roman", serif;
    font-size: 14px;
    line-height: 24px;
    letter-spacing: 1px;
  }
  .wine-title {
    position: absolute;
    left: 0;
    right: 0;
    top: 515px;
    font-family: "Herr Von Muellerhoff", cursive;
    font-weight: 400;
    font-size: 64px;
    line-height: 90px;
  }
  .wine-title span { display: block; }
</style>
</head>
<body>
  <main class="canvas">
    <section class="wine-label">
      <div class="estate-illustration" role="img" aria-label="Gold engraved illustration of the estate homestead framed by three tall palm trees"></div>
      <h1 class="winery-name">
        <span>Marrow Creek</span>
        <span>Vineyards</span>
      </h1>
      <div class="vintage">2012</div>
      <h2 class="wine-title">
        <span>The Quiet Harvest</span>
        <span>Shiraz-Cabernet</span>
      </h2>
    </section>
  </main>
</body>
</html>
```